Bath Salt Packaging

Hello! We are Dr Velbo Organics, a company providing the best and most nutritious food and health-care products for the health conscious around the world!
We are currently in the process of releasing a few new products, one of which is Himalayan Bath Salt Crystals. It is an ancient, pure salt which has been protected from environmental toxins and pollution under the Himalayan mountains for more than 250 million years!
Our salt is 100% pure and unrefined, still containing the original mineral composition of the ancient life-giving ocean that supported our early ancestors. There are over 60 trace minerals in this salt, the majority of which exist in colloidal forms, meaning they are highly bioavailable and quickly ionized when added to water.
So, we need packaging designed for our four salt packets; a 300mL jar, a 150mL jar, a 10g sachet and a box which will house the sachets. I have attached the label content, measurements and a little extra instruction/information.
We want a natural, eco-friendly feel for the packaging. Thanks!
ps. please use the 3rd of the Logo's (TM, 'Organics' under leaf)

```html
<!DOCTYPE html>
<html lang="en">
<head>
<meta charset="utf-8">
<title>Himalayan Bath Salt Crystals – Jar Label 300mL</title>
<link href="https://fonts.googleapis.com/css2?family=Bebas+Neue&family=Open+Sans:wght@400;700&family=Parisienne&display=swap" rel="stylesheet">
<style>
  :root {
    --page-bg: #ffffff;
    --label-bg: #fbfbfa;
    --wood-light: #efece8;
    --wood-mid: #ddd6cf;
    --salt-pink: #e9b9a4;
    --salt-deep: #d98f74;
    --brand-green: #6cb33f;
    --seal-green: #8cc63f;
    --ink-dark: #2a4030;
    --ink-grey: #444a46;
  }
  * { margin: 0; padding: 0; box-sizing: border-box; }
  html, body {
    width: 1200px;
    height: 961px;
    overflow: hidden;
    background: var(--page-bg);
  }
  .canvas {
    position: relative;
    width: 1200px;
    height: 961px;
  }
  .jar-label {
    position: absolute;
    left: 355px;
    top: 55px;
    width: 490px;
    height: 850px;
    background: var(--label-bg);
    overflow: hidden;
    box-shadow: 0 0 0 1px #e6e6e4;
  }
  .hero-photo {
    position: absolute;
    inset: 0 0 auto 0;
    height: 560px;
    background:
      radial-gradient(ellipse 120px 90px at 62% 8%, var(--salt-deep), transparent 75%),
      radial-gradient(ellipse 100px 90px at 14% 36%, var(--salt-pink), transparent 75%),
      linear-gradient(180deg, var(--wood-mid) 0%, var(--wood-light) 55%, var(--label-bg) 100%);
  }
  .quality-seal {
    position: absolute;
    left: 215px;
    top: 111px;
    width: 234px;
    height: 234px;
    border-radius: 50%;
    background: var(--seal-green);
    border: 5px solid #ffffff;
  }
  .brand-name {
    position: absolute;
    top: 446px;
    width: 100%;
    text-align: center;
    font-family: "Open Sans", sans-serif;
    font-weight: 400;
    font-size: 30px;
    line-height: 1.2;
    color: var(--ink-grey);
    letter-spacing: 0.5px;
  }
  .product-name {
    position: absolute;
    top: 548px;
    width: 100%;
    text-align: center;
    font-family: "Parisienne", cursive;
    font-weight: 400;
    font-size: 88px;
    line-height: 1;
    color: var(--ink-dark);
  }
  .product-type {
    position: absolute;
    top: 654px;
    width: 100%;
    text-align: center;
    font-family: "Bebas Neue", sans-serif;
    font-weight: 400;
    font-size: 64px;
    line-height: 1;
    color: var(--brand-green);
    letter-spacing: -0.5px;
  }
  .net-volume {
    position: absolute;
    top: 794px;
    width: 100%;
    text-align: center;
    font-family: "Open Sans", sans-serif;
    font-size: 22px;
    line-height: 1.2;
    color: var(--ink-dark);
  }
  .net-volume strong { font-weight: 700; }
</style>
</head>
<body>
<main class="canvas">
  <section class="jar-label">
    <div class="hero-photo" role="img" aria-label="Photograph of pink Himalayan salt crystals in wooden bowls beside a brass mortar and pestle on whitewashed wood"></div>
    <div class="quality-seal" role="img" aria-label="Quality seal"></div>

    <p class="brand-name">Dr Velbo Organics</p>
    <h1 class="product-name">Himalayan</h1>
    <h2 class="product-type">Bath Salt Crystals</h2>
    <p class="net-volume"><strong>300</strong>mL</p>
  </section>
</main>
</body>
</html>
```